Business card for exciting VC company

Should look simple, crisp, and modern.

Industry/Entity Type

Venture Capital

Contact Information for Business Card

Would like to see at least one design that has our blue on the back with the tagline "Transforming Traditional Industry" and white front with contact details.

Font styles to use
Sans Serif

Requirements
Must have
• Logo

Gregory Tallis
gtallis@brindlewave.vc
Managing Partner
M (628)354-xxxx

```html
<!DOCTYPE html>
<html lang="en">
<head>
<meta charset="utf-8">
<title>Brindlewave Capital – Business Card</title>
<link rel="stylesheet" href="https://fonts.googleapis.com/css2?family=Montserrat:wght@500;600&family=Lato:wght@400;700&family=Arimo:wght@400&display=swap">
<style>
  :root {
    --stage: #2a2a2c;
    --brand-blue: #4284c6;
    --card-white: #ffffff;
    --ink: #141414;
    --divider: #c9c9c9;
    --tagline: #ffffff;
  }
  * { box-sizing: border-box; margin: 0; padding: 0; }
  html, body {
    width: 1200px; height: 900px; overflow: hidden;
    background: var(--stage);
  }
  .stage {
    width: 1200px; height: 900px;
    display: flex; flex-direction: column;
    align-items: center; justify-content: center; gap: 56px;
  }
  .card {
    width: 560px; height: 320px; position: relative;
    box-shadow: 0 12px 30px rgba(0,0,0,.45);
  }
  /* Back */
  .card-back {
    background: var(--brand-blue);
    display: flex; flex-direction: column; align-items: center; justify-content: center;
  }
  .wordmark {
    font-family: "Montserrat", sans-serif; font-weight: 500;
    letter-spacing: 0.12em; text-transform: uppercase;
    white-space: nowrap;
  }
  .card-back .wordmark { color: var(--card-white); font-size: 32px; margin-top: -20px; }
  .tagline {
    position: absolute; bottom: 38px; left: 0; right: 0; text-align: center;
    font-family: "Lato", sans-serif; font-weight: 700; font-size: 12px;
    letter-spacing: 0.06em; color: var(--tagline); text-transform: uppercase;
  }
  /* Front */
  .card-front {
    background: var(--card-white);
    display: grid; grid-template-columns: 320px 1fr;
  }
  .front-brand {
    display: flex; align-items: center; justify-content: center;
    padding: 70px 20px 0 28px;
  }
  .front-brand .wordmark { color: var(--ink); font-size: 18px; letter-spacing: 0.1em; }
  .front-details {
    border-left: 1px solid var(--divider);
    margin: 40px 0 90px;
    padding: 20px 0 0 24px;
  }
  .person-name {
    font-family: "Montserrat", sans-serif; font-weight: 600; font-size: 17px;
    color: var(--brand-blue); text-transform: uppercase; letter-spacing: 0.01em;
    white-space: nowrap;
  }
  .person-title {
    font-family: "Arimo", sans-serif; font-size: 14px; color: var(--ink); margin-bottom: 14px;
  }
  .contact-list { list-style: none; }
  .contact-list li {
    display: flex; align-items: center; gap: 8px;
    font-family: "Arimo", sans-serif; font-size: 13.5px; color: var(--ink);
    line-height: 22px; white-space: nowrap;
  }
  .contact-icon { width: 15px; height: 15px; flex: none; }
</style>
</head>
<body>
<main class="stage">
  <section class="card card-back">
    <div class="wordmark">Brindlewave Capital</div>
    <p class="tagline">Transforming Traditional Industry</p>
  </section>

  <section class="card card-front">
    <div class="front-brand">
      <div class="wordmark">Brindlewave Capital</div>
    </div>
    <div class="front-details">
      <h1 class="person-name">Gregory Tallis</h1>
      <p class="person-title">Managing Partner</p>
      <ul class="contact-list">
        <li>
          <svg class="contact-icon" viewBox="0 0 24 24" aria-hidden="true"><path fill="#4284c6" d="M6.6 10.8c1.4 2.8 3.8 5.1 6.6 6.6l2.2-2.2c.3-.3.7-.4 1-.2 1.1.4 2.3.6 3.6.6.6 0 1 .4 1 1V20c0 .6-.4 1-1 1C10.6 21 3 13.4 3 4c0-.6.4-1 1-1h3.5c.6 0 1 .4 1 1 0 1.3.2 2.5.6 3.6.1.3 0 .7-.2 1z"/></svg>
          (628)354-xxxx
        </li>
        <li>
          <svg class="contact-icon" viewBox="0 0 24 24" aria-hidden="true"><rect x="2" y="5" width="20" height="14" fill="#4284c6"/><path d="M2 5l10 8 10-8" fill="none" stroke="#fff" stroke-width="1.6"/></svg>
          gtallis@brindlewave.vc
        </li>
        <li>
          <svg class="contact-icon" viewBox="0 0 24 24" aria-hidden="true"><g fill="none" stroke="#4284c6" stroke-width="2"><circle cx="12" cy="12" r="9.5"/><ellipse cx="12" cy="12" rx="4.5" ry="9.5"/><path d="M2.5 12h19M4.5 7h15M4.5 17h15"/></g></svg>
          www.brindlewave.vc
        </li>
      </ul>
    </div>
  </section>
</main>
</body>
</html>
```